新設法人による新規名刺作成です。
一般顧客が主ですので、基本はシンプルで分かり易いデザインがいいかと思いますが、特にこだわりません。
私がいいと思っている一例の画像添付しますが、他に良い案あればご提案ください。
記載項目
【会社情報】
社名)クレスト・ピア株式会社
氏名)坂口 典彦
役職)代表取締役
資格)宅地建物取引士、一級建築士
住所)奈良県橿原市翠峰町207-4-3
TEL)0744-68-5172
FAX)0744-68-5173
MAIL)crestpier@desk.kumovia.ne.jp

【許可情報】
建設業許可)奈良県知事(般-27)第05876号
宅建免許)奈良県知事(1)第0587号

【業務内容】※レイアウトのバランス悪ければ記載不要
・住宅/店舗/事務所等 各種施設施工
・リフォーム
・分譲住宅販売
・土地建物 仲介/賃貸/売買/利活用

許可番号や氏名等、随時変更しますので、編集しやすいデータ形式で納品お願いします。

最終的な決め手はデザイン力であったと思います。
限られてレイアウトの中で、良い提案をしていただきました。

たくさんの良い提案ありがとうございます。
またこちらのお願いも快く引き受けていただき感謝申し上げます。

今回ご縁ございませんでしたが、また機会ございましたら宜しくお願い致します。

```html
<!DOCTYPE html>
<html lang="ja">
<head>
<meta charset="utf-8">
<title>クレスト・ピア株式会社 名刺</title>
<link rel="stylesheet" href="https://fonts.googleapis.com/css2?family=Noto+Sans+JP:wght@400;500;700&display=swap">
<style>
  :root {
    --brand-blue: #1f86d3;
    --brand-navy: #1c3f8f;
    --ink: #333538;
    --paper: #ffffff;
    --backdrop: #e9ebee;
  }
  * { margin: 0; padding: 0; box-sizing: border-box; }
  html, body { width: 1200px; height: 876px; overflow: hidden; }
  body {
    background: var(--backdrop);
    font-family: "Noto Sans JP", sans-serif;
    color: var(--ink);
    position: relative;
  }
  .card {
    position: absolute;
    width: 640px;
    height: 387px;
    background: var(--paper);
    box-shadow: 0 6px 18px rgba(0,0,0,.18);
    overflow: hidden;
  }

  /* back side */
  .card-back { left: 100px; top: 30px; }
  .card-back .blue-field {
    position: absolute; left: 0; top: 0; width: 100%; height: 250px;
    background: var(--brand-blue); color: var(--paper);
    display: flex; flex-direction: column; align-items: center;
  }
  .card-back .brand {
    margin-top: 78px; display: flex; align-items: center; gap: 14px;
  }
  .card-back .brand-square {
    width: 38px; height: 38px; background: var(--paper);
  }
  .card-back .brand-name {
    font-size: 40px; font-weight: 700; letter-spacing: 1px; line-height: 1;
  }
  .card-back .brand-kana {
    font-size: 13px; margin-top: 6px; letter-spacing: 2px; padding-left: 52px;
  }
  .card-back .licenses {
    margin-top: auto; margin-bottom: 20px;
    display: flex; gap: 28px; font-size: 12px; letter-spacing: .5px;
  }
  .card-back .services {
    position: absolute; left: 0; top: 250px; width: 100%; height: 137px;
    display: flex; flex-direction: column; align-items: center; justify-content: center;
    font-size: 13px; line-height: 1.8; text-align: center;
  }
  .card-back .services-title { font-weight: 700; }

  /* front side */
  .card-front { left: 460px; top: 452px; }
  .card-front .brand-area {
    position: absolute; left: 0; top: 0; width: 250px; height: 100%;
    display: flex; flex-direction: column; align-items: center; justify-content: center;
  }
  .card-front .brand-square {
    width: 78px; height: 78px; background: var(--brand-blue); margin-bottom: 20px;
  }
  .card-front .brand-name {
    font-size: 36px; font-weight: 700; color: var(--ink); line-height: 1;
  }
  .card-front .brand-kana {
    font-size: 12px; margin-top: 6px; letter-spacing: 2px; color: var(--ink);
  }
  .card-front .info-panel {
    position: absolute; left: 250px; top: 0; right: 0; bottom: 0;
    background: var(--brand-blue); color: var(--paper);
    border-top-left-radius: 10px; border-bottom-left-radius: 10px;
    padding: 34px 30px 0 34px;
  }
  .person-title { font-size: 13px; }
  .person-name-row { display: flex; align-items: baseline; gap: 18px; margin-top: 6px; }
  .person-name { font-size: 28px; font-weight: 500; letter-spacing: 8px; }
  .person-roman { font-size: 13px; }
  .person-licences { font-size: 13px; margin-top: 12px; }
  .company-name { font-size: 17px; font-weight: 700; margin-top: 46px; }
  .contact { font-style: normal; font-size: 14px; line-height: 1.45; margin-top: 14px; letter-spacing: .3px; }
</style>
</head>
<body>

<section class="card card-back" aria-label="名刺 裏面">
  <div class="blue-field">
    <div class="brand">
      <span class="brand-square"></span>
      <span class="brand-name">crest pier</span>
    </div>
    <div class="brand-kana">クレスト・ピア株式会社</div>
    <div class="licenses">
      <span>建設業許可 奈良県知事(般-27)第05876号</span>
      <span>宅建免許 奈良県知事(1)第0587号</span>
    </div>
  </div>
  <div class="services">
    <p class="services-title">【業務内容】</p>
    <p>住宅/店舗/事務所等 各種施設施工・リフォーム</p>
    <p>分譲住宅販売・土地建物 仲介/賃貸/売買/利活用</p>
  </div>
</section>

<section class="card card-front" aria-label="名刺 表面">
  <div class="brand-area">
    <span class="brand-square"></span>
    <span class="brand-name">crest pier</span>
    <span class="brand-kana">クレスト・ピア株式会社</span>
  </div>
  <div class="info-panel">
    <p class="person-title">代表取締役</p>
    <div class="person-name-row">
      <span class="person-name">坂口 典彦</span>
      <span class="person-roman">Norihiko Sakaguchi</span>
    </div>
    <p class="person-licences">宅地建物取引士 / 一級建築士</p>
    <p class="company-name">クレスト・ピア 株式会社</p>
    <address class="contact">
      〒634-0052<br>
      奈良県橿原市翠峰町207-4-3<br>
      TEL 0744-68-5172<br>
      FAX 0744-68-5173<br>
      E-mail crestpier@desk.kumovia.ne.jp
    </address>
  </div>
</section>

</body>
</html>
```